Online Travel Agency card design with 2 logos

Need a two sided business card design for online tourism agency which is based in Istanbul Turkey.
Need a business card design where it shows the travel agency logo but also the logo and information of the parent company as well.Parent company logo is just text with 2 different colors. (Arial font with text ToreVextra "Tore"- hex #172841 and "Vextra" hex-#FF7F00)
Both logos are uploaded.
Target Market(s)
travel , online
Industry/Entity Type
Travel
Contact Information for Business Card
The information on the card should be as :
Travel Agency Logo logo (pnlogo)
Parent Company logo(torelogo)
Company information :ToreVextra Turizm ve Bilgi Teknolojileri A.Ş
Address of company
Tel
Email
Name
Position(english and turkish)

```html
<!DOCTYPE html>
<html lang="tr">
<head>
<meta charset="utf-8">
<title>ToreVextra Business Card</title>
<link rel="stylesheet" href="https://fonts.googleapis.com/css2?family=Arimo:wght@700&family=Open+Sans:wght@400;600;700&display=swap">
<style>
  :root {
    --navy: #172841;
    --orange: #ff7f00;
    --white: #ffffff;
    --ink: #1b2238;
    --pattern: #1f3251;
    --bg-top: #626262;
    --bg-bottom: #727272;
  }
  * { margin: 0; padding: 0; box-sizing: border-box; }
  html, body { width: 1200px; height: 900px; overflow: hidden; }
  body {
    position: relative;
    background: linear-gradient(180deg, var(--bg-top), var(--bg-bottom));
    font-family: "Open Sans", Arial, sans-serif;
  }
  .card {
    position: absolute;
    top: 306px;
    height: 271px;
    border-radius: 10px;
    overflow: hidden;
    box-shadow: 0 2px 6px rgba(0,0,0,0.25);
  }
  .card--front { left: 149px; width: 439px; background: var(--navy); }
  .card--back { left: 608px; width: 441px; background: var(--navy); }

  .front__top {
    position: absolute; left: 0; top: 0; width: 100%; height: 146px;
    background: var(--white);
    border-bottom: 6px solid var(--orange);
  }
  .parent-logo {
    position: absolute; left: 23px; top: 45px;
    font-family: "Arimo", Arial, sans-serif; font-weight: 700;
    font-size: 38px; letter-spacing: 0.2px; color: var(--navy);
  }
  .person { position: absolute; right: 21px; top: 25px; text-align: right; color: var(--ink); }
  .person__name { font-size: 15px; font-weight: 600; line-height: 19px; }
  .person__role { font-size: 12px; line-height: 15.5px; }
  .agency-logo {
    position: absolute; right: 21px; top: 92px;
    display: flex; align-items: center; gap: 3px;
  }
  .agency-logo__dot { width: 25px; height: 25px; border-radius: 50%; background: var(--navy); }
  .agency-logo__name { font-size: 21px; font-weight: 600; color: var(--navy); letter-spacing: -0.3px; }

  .company { position: absolute; left: 24px; top: 173px; }
  .company__name { color: var(--orange); font-size: 11.5px; font-weight: 700; line-height: 16px; }
  .company__address { margin-top: 5px; color: var(--white); font-size: 12.5px; line-height: 16px; }
  .contact { position: absolute; right: 22px; top: 208px; color: var(--white); font-size: 12.5px; line-height: 16px; }
  .contact__row { display: flex; justify-content: flex-end; align-items: center; gap: 6px; }
  .contact__icon { width: 10px; height: 10px; }

  .pattern {
    position: absolute; left: 7px; top: 0;
    font-family: "Arimo", Arial, sans-serif; font-weight: 700;
    font-size: 21px; color: var(--pattern);
  }
  .pattern__row { display: flex; gap: 57px; height: 39px; line-height: 22px; padding-top: 1px; white-space: nowrap; }
  .back-logo {
    position: absolute; left: 0; right: 0; top: 110px; text-align: center;
    font-family: "Arimo", Arial, sans-serif; font-weight: 700;
    font-size: 48px; color: var(--white);
  }
</style>
</head>
<body>
  <section class="card card--front">
    <div class="front__top">
      <div class="parent-logo">ToreVextra</div>
      <div class="person">
        <div class="person__name">Dorian Vell</div>
        <div class="person__role">Managing Director</div>
        <div class="person__role">Genel müdür</div>
      </div>
      <div class="agency-logo">
        <span class="agency-logo__dot"></span>
        <span class="agency-logo__name">yolaria</span>
      </div>
    </div>
    <div class="company">
      <div class="company__name">ToreVextra Turizm<br>ve Bilgi Teknolojileri A.Ş</div>
      <div class="company__address">1234, Address GoesHere,<br>Country name, 12345</div>
    </div>
    <div class="contact">
      <div class="contact__row">
        <span>(044)123456789</span>
        <svg class="contact__icon" viewBox="0 0 10 10" aria-hidden="true"><path d="M2 0.5 L3.6 2.6 L2.8 3.6 C3.4 5 4.8 6.4 6.3 7.1 L7.3 6.3 L9.5 7.9 L8.4 9.5 C4.6 9.2 0.8 5.4 0.5 1.6 Z" fill="var(--orange)"/></svg>
      </div>
      <div class="contact__row">
        <span>info@youremail.com</span>
        <svg class="contact__icon" viewBox="0 0 10 10" aria-hidden="true"><rect x="0.5" y="2" width="9" height="6.5" fill="var(--orange)"/><path d="M0.8 2.3 L5 5.6 L9.2 2.3" stroke="var(--navy)" stroke-width="0.9" fill="none"/></svg>
      </div>
    </div>
  </section>

  <section class="card card--back">
    <div class="pattern" aria-hidden="true">
      <div class="pattern__row"><span>ToreVextra</span><span>ToreVextra</span><span>ToreVextra</span></div>
      <div class="pattern__row"><span>ToreVextra</span><span>ToreVextra</span><span>ToreVextra</span></div>
      <div class="pattern__row"><span>ToreVextra</span><span>ToreVextra</span><span>ToreVextra</span></div>
      <div class="pattern__row"><span>ToreVextra</span><span>ToreVextra</span><span>ToreVextra</span></div>
      <div class="pattern__row"><span>ToreVextra</span><span>ToreVextra</span><span>ToreVextra</span></div>
      <div class="pattern__row"><span>ToreVextra</span><span>ToreVextra</span><span>ToreVextra</span></div>
      <div class="pattern__row"><span>ToreVextra</span><span>ToreVextra</span><span>ToreVextra</span></div>
    </div>
    <div class="back-logo">ToreVextra</div>
  </section>
</body>
</html>
```